New website design for small car detailing company.

We have a small cleaning company, our main focus is car detailing but we are also expanding to home and residential cleaning and power washing.
I would like the web site to have a simple layout and SEO friendly.
I would also like to have a contact page in which clients can contact us and upload pictures of the house or car so we can provide an estimate.
A Page that shows the services we offer.

Target Market(s)

High paying clients for car detailiing and focus on residential and commercial cleaning.

Industry/Entity Type

Cleaning Service

Coding

Coded - Design and coding required

Number of Pages Required

4 page

Font styles to use
Serif

Colors

Designer to choose only greyscale colors for use in the design.

Requirements
Must have
• A home page.
Blog page for SEO
Contact page with the choice of clients to upload theirs pictures so we can provide estimates with calendar integration so they can provide their available dates for service.
A pictures to sell our services.
Nice to have
• Simple but sleek desing, I am more interested in SEO Score than heavy loads

```html
<!DOCTYPE html>
<html lang="en">
<head>
<meta charset="utf-8">
<title>Pinecrest Mobile Detailing</title>
<link href="https://fonts.googleapis.com/css2?family=Oswald:wght@400;500;600&family=Montserrat:wght@400;500&display=swap" rel="stylesheet">
<style>
:root{
  --ink:#0d0d0d;
  --black:#111111;
  --white:#ffffff;
  --mist:#ececec;
  --paper:#f4f4f4;
  --grey:#555555;
  --line:#2c2c2c;
  --soft:#9a9a9a;
}
*{box-sizing:border-box;margin:0;padding:0}
html,body{width:1200px;height:2836px;overflow:hidden}
body{position:relative;background:var(--white);font-family:'Montserrat',sans-serif;color:var(--ink)}
.abs{position:absolute}
.backdrop{position:absolute;left:0;top:0}
.head{font-family:'Oswald',sans-serif;text-transform:uppercase}
.nav a{font-family:'Oswald',sans-serif;font-size:14px;letter-spacing:2.5px;color:var(--ink);text-decoration:none;position:absolute;top:35px}
.brand{position:absolute;left:520px;top:30px;width:160px;text-align:center;font-family:'Oswald',sans-serif;font-weight:600;font-size:17px;line-height:20px;letter-spacing:1px;color:var(--ink)}
.btn-dark{position:absolute;background:var(--ink);color:var(--white);font-family:'Oswald',sans-serif;font-size:14px;letter-spacing:2.5px;display:flex;align-items:center;justify-content:center;gap:10px}
.btn-line{position:absolute;border:1px solid var(--ink);color:var(--ink);font-family:'Oswald',sans-serif;font-size:14px;letter-spacing:2.5px;display:flex;align-items:center;justify-content:center;gap:10px}
.body-text{font-size:12.5px;line-height:19px;color:#333}
.center{text-align:center;left:0;width:1200px}
.section-title{font-family:'Oswald',sans-serif;font-size:28px;letter-spacing:6px;font-weight:500}
.photo{position:absolute}
.card-bar{position:absolute;left:0;bottom:0;width:100%;height:58px;background:rgba(0,0,0,.78);display:flex;align-items:center;justify-content:space-between;padding:0 14px 0 21px}
.card-bar span{font-family:'Oswald',sans-serif;color:var(--white);font-size:16px;line-height:19px}
.card-arrow{width:41px;height:26px;background:var(--white);display:flex;align-items:center;justify-content:center}
.round-arrow{position:absolute;width:44px;height:44px;border-radius:50%;background:#2a2a2a;display:flex;align-items:center;justify-content:center}
.checks li{list-style:none;display:flex;align-items:center;gap:8px;font-size:12px;font-weight:500;height:32px}
.tick{width:24px;height:24px;border:1px solid var(--ink);border-radius:50%;display:flex;align-items:center;justify-content:center}
.stat{position:absolute;top:1570px;display:flex;align-items:center;gap:14px;color:var(--white)}
.stat b{display:block;font-family:'Oswald',sans-serif;font-size:32px;font-weight:500;line-height:36px}
.stat small{display:block;font-family:'Oswald',sans-serif;font-size:16px;text-transform:uppercase}
.foot-nav a{position:absolute;left:903px;font-family:'Oswald',sans-serif;font-size:12px;letter-spacing:2px;color:var(--white);text-decoration:none}
.foot-info{position:absolute;left:142px;color:var(--white);font-size:12px;display:flex;gap:10px;line-height:19px}
</style>
</head>
<body>

<svg class="backdrop" width="1200" height="2836" aria-hidden="true">
  <rect x="0" y="470" width="1200" height="540" fill="var(--black)"/>
  <path d="M0 0H1200V490Q600 600 0 490Z" fill="var(--mist)"/>
  <path d="M0 0H420Q200 20 0 60Z" fill="var(--white)"/>
  <path d="M1200 0H780Q1000 20 1200 60Z" fill="var(--white)"/>
  <path d="M0 915Q600 760 1200 915V1010H0Z" fill="var(--white)"/>
  <rect x="0" y="1600" width="1200" height="420" fill="var(--paper)"/>
  <rect x="0" y="2240" width="1200" height="596" fill="var(--black)"/>
</svg>

<!-- header -->
<nav class="nav">
  <a style="left:143px">HOME</a>
  <a style="left:214px">SERVICES ▾</a>
  <a style="left:311px">BLOG</a>
  <a style="left:380px">CONTACT US</a>
</nav>
<div class="brand">PINECREST<br>MOBILE<br>DETAILING</div>
<div class="abs head" style="left:725px;top:35px;font-size:14px;letter-spacing:2px;display:flex;gap:6px;align-items:center">
  <svg width="12" height="14" viewBox="0 0 12 14"><path d="M2 1l3 3-1.5 2a8 8 0 0 0 4 4l2-1.5 3 3-2 2C5 13 -1 7 0 3z" fill="none" stroke="#111" stroke-width="1"/></svg>+1 555-014-2286
</div>
<div class="btn-dark" style="left:907px;top:26px;width:149px;height:33px">GET A QUOTE <span>→</span></div>

<!-- hero -->
<div class="abs head" style="left:142px;top:210px;font-size:15px;letter-spacing:3px;display:flex;align-items:center;gap:8px"><span style="width:20px;height:1px;background:#111;display:inline-block"></span>ENHANCE YOUR CAR</div>
<h1 class="abs head" style="left:142px;top:230px;font-size:40px;font-weight:500;letter-spacing:.5px">LIKE A BRAND NEW</h1>
<p class="abs body-text" style="left:142px;top:286px;width:330px">Lorem ipsum dolor sit amet, consectetur adipiscing elit. Aenean sed efficitur nunc. Nulla sed leo nulla. In lobortis, ipsum lacinia vulputate feugiat,</p>
<div class="btn-line" style="left:142px;top:364px;width:163px;height:37px">VIEW SERVICES <span>→</span></div>
<div class="photo" role="img" aria-label="Silver sedan shown in three-quarter front view" style="left:550px;top:195px;width:505px;height:260px;border-radius:45% 45% 20% 20%;background:radial-gradient(ellipse at 55% 50%,#c9cbd0,#a9acb3 55%,rgba(236,236,236,0) 72%)"></div>
<div class="abs" style="left:567px;top:499px;display:flex;gap:8px">
  <span style="width:17px;height:2px;background:#bbb"></span><span style="width:17px;height:3px;background:#111"></span><span style="width:17px;height:2px;background:#bbb"></span>
</div>

<!-- services -->
<h2 class="abs section-title center" style="top:592px;color:var(--white)">OUR SERVICES</h2>
<p class="abs body-text center" style="top:640px;color:#ddd;padding:0 215px">Orci varius natoque penatibus et magnis dis parturient montes, nascetur ridiculus mus. Cras tincidunt sed elit at posuere. Sed vestibu lum consectetur odio id ultricies. Ut blandit, magna a mollis fringilla, purus purus eleifend metus,</p>

<div class="photo" role="img" aria-label="Detailer polishing a car headlight with a yellow cloth" style="left:143px;top:720px;width:284px;height:280px;background:linear-gradient(135deg,#d8b27a,#8f7a60 50%,#2a2a2a)">
  <div class="card-bar"><span>MOBILE DETAILING</span><div class="card-arrow">→</div></div>
</div>
<div class="photo" role="img" aria-label="Gloved hands cleaning a car dashboard" style="left:457px;top:720px;width:285px;height:280px;background:linear-gradient(135deg,#6f8a6e,#3a3a3a 45%,#b7b7b7 75%,#c85a6a)">
  <div class="card-bar"><span>INTERIOR/EXTERIOR DETAILS</span><div class="card-arrow">→</div></div>
</div>
<div class="photo" role="img" aria-label="Hand wiping a window with spray and cloth" style="left:772px;top:720px;width:285px;height:280px;background:linear-gradient(135deg,#e8e8ee,#c8d4e4 50%,#7aa3c7)">
  <div class="card-bar"><span>RESIDENTIAL/COMMERCIAL<br>HOUSE CLEANING</span><div class="card-arrow">→</div></div>
</div>
<div class="round-arrow" style="left:121px;top:816px"><svg width="16" height="10"><path d="M15 5H1M5 1L1 5l4 4" stroke="#fff" fill="none"/></svg></div>
<div class="round-arrow" style="left:1033px;top:816px"><svg width="16" height="10"><path d="M1 5h14M11 1l4 4-4 4" stroke="#fff" fill="none"/></svg></div>

<!-- what we do -->
<h2 class="abs section-title center" style="top:1050px">WHAT WE DO</h2>
<p class="abs body-text center" style="top:1098px">Orci varius natoque penatibus et magnis dis parturient montes, nascetur ridiculus mus. Cras tincidunt sed elit at posuere.</p>
<p class="abs body-text" style="left:142px;top:1157px;width:432px">Lorem ipsum dolor sit amet, consectetur adipiscing elit. Aenean sed efficit ur nunc. Nulla sed leo nulla. In lobortis, ipsum lacinia vulputate feugiat, Nullam venenatis, enim sit amet malesuada commodo, diam tortor efficitur purus, sit amet commodo purus tortor sit amet augue. Vestibulum quis effi citur quam, a volutpat dolor.</p>
<ul class="abs checks" style="left:142px;top:1269px">
  <li><span class="tick"><svg width="10" height="8"><path d="M1 4l3 3 5-6" stroke="#111" fill="none"/></svg></span>Ut dolor metus, elementum sit amet sem vel.</li>
  <li><span class="tick"><svg width="10" height="8"><path d="M1 4l3 3 5-6" stroke="#111" fill="none"/></svg></span>Pulvinar imperdiet orci. Cras mattis nisi ut convallis faucibus.</li>
  <li><span class="tick"><svg width="10" height="8"><path d="M1 4l3 3 5-6" stroke="#111" fill="none"/></svg></span>Rellentesque dapibus quam nec vestibulum fringilla.</li>
  <li><span class="tick"><svg width="10" height="8"><path d="M1 4l3 3 5-6" stroke="#111" fill="none"/></svg></span>Aroin sollicitudin lacus ac dui facilisis, ac sollicitudin dales.</li>
</ul>
<div class="btn-line" style="left:142px;top:1428px;width:163px;height:37px">CONTACT US <span>→</span></div>
<div class="photo" role="img" aria-label="Detailer in a branded black shirt standing beside a white SUV" style="left:653px;top:1165px;width:401px;height:300px;background:linear-gradient(100deg,#cfd3d6,#8d9398 35%,#1c1c1c 55%,#101010)"></div>

<!-- stats -->
<div class="photo" role="img" aria-label="Dark close-up of a car front grille" style="left:143px;top:1512px;width:914px;height:197px;background:linear-gradient(180deg,#1e1e1e,#0e0e0e 60%,#242424)"></div>
<div class="abs" style="left:487px;top:1540px;width:1px;height:130px;background:var(--line)"></div>
<div class="abs" style="left:750px;top:1540px;width:1px;height:130px;background:var(--line)"></div>
<div class="stat" style="left:240px">
  <svg width="62" height="62" viewBox="0 0 62 62" fill="none" stroke="#fff" stroke-width="2"><path d="M6 26l6-14h26l6 14v14H6z"/><circle cx="14" cy="40" r="4"/><circle cx="36" cy="40" r="4"/><path d="M46 30h10v28H46zM6 46h18v12H6z"/></svg>
  <div><b>754</b><small>Vehicles Serviced</small></div>
</div>
<div class="stat" style="left:532px">
  <svg width="50" height="62" viewBox="0 0 50 62" fill="none" stroke="#fff" stroke-width="2"><circle cx="25" cy="18" r="11"/><path d="M4 58c0-14 9-22 21-22s21 8 21 22z"/></svg>
  <div><b>675</b><small>Happy Clients</small></div>
</div>
<div class="stat" style="left:806px">
  <svg width="54" height="54" viewBox="0 0 54 54" fill="none" stroke="#fff" stroke-width="2"><path d="M2 22h12v30H2zM14 24l10-14c2-4 7-3 7 2l-2 10h18c4 0 5 4 4 7l-5 17c-1 3-3 4-6 4H14"/></svg>
  <div><b>1215</b><small>People Likes</small></div>
</div>

<!-- residential -->
<h2 class="abs section-title" style="left:143px;top:1770px;font-size:27px;line-height:28px;letter-spacing:7px">RESIDENTIAL AND COMMERCIAL<br>CLEANING &amp; POWER WASHING</h2>
<div class="btn-dark" style="left:907px;top:1779px;width:149px;height:33px">GET A QUOTE <span>→</span></div>
<p class="abs body-text" style="left:142px;top:1851px;width:432px">Lorem ipsum dolor sit amet, consectetur adipiscing elit. Aenean sed efficit ur nunc. Nulla sed leo nulla. In lobortis, ipsum lacinia vulputate feugiat, Nullam venenatis, enim sit amet malesuada commodo, diam tortor efficitur purus, sit amet commodo purus tortor sit amet augue. Vestibulum quis effi citur quam, a volutpat dolor.</p>
<p class="abs body-text" style="left:623px;top:1851px;width:434px">Orci varius natoque penatibus et magnis dis parturient montes, nascetur ridiculus mus. Cras tincidunt sed elit at posuere. Sed vestibulum consectet ur odio id ultricies. Ut blandit, magna a mollis fringilla, purus purus eleifend metus, in convallis ex lacus vestibulum metus.</p>

<svg class="backdrop" width="1200" height="2836" aria-hidden="true" style="z-index:0">
  <defs>
    <clipPath id="band"><path d="M0 1960Q600 2060 1200 1960V2255Q600 2370 0 2255Z"/></clipPath>
    <linearGradient id="floor" x1="0" y1="0" x2="1" y2="1"><stop offset="0" stop-color="#c9cfd4"/><stop offset=".5" stop-color="#b87a5c"/><stop offset="1" stop-color="#8c949a"/></linearGradient>
    <linearGradient id="room" x1="0" y1="0" x2="1" y2="1"><stop offset="0" stop-color="#d8d4cc"/><stop offset=".5" stop-color="#b7b3ad"/><stop offset="1" stop-color="#e8e2d8"/></linearGradient>
  </defs>
  <g clip-path="url(#band)">
    <rect x="0" y="1950" width="600" height="430" fill="url(#floor)" role="img" aria-label="Floor scrubbing machine polishing a tiled commercial floor"/>
    <rect x="600" y="1950" width="600" height="430" fill="url(#room)" role="img" aria-label="Cleaner vacuuming a rug in a bright living room"/>
  </g>
</svg>
<div class="abs" style="left:538px;top:2088px;width:124px;height:124px;border-radius:50%;background:var(--white);display:flex;align-items:center;justify-content:center;text-align:center;font-family:'Oswald',sans-serif;font-weight:600;font-size:14px;line-height:17px;color:var(--ink)">PINECREST<br>MOBILE<br>DETAILING</div>

<!-- newsletter & footer -->
<h3 class="abs head" style="left:140px;top:2362px;font-size:17px;letter-spacing:3px;color:var(--white);font-weight:500">SUBCRIBE TO OUR NEWSLETTER</h3>
<p class="abs body-text" style="left:140px;top:2392px;width:430px;color:#ccc">Orci varius natoque penatibus et magnis dis parturient montes, nascetur ridiculus mus. Cras tincidunt sed elit at posuere. Sed vestib</p>
<div class="abs" style="left:649px;top:2380px;width:267px;height:46px;background:#2e2e2e;display:flex;align-items:center;gap:10px;padding-left:18px;font-size:11px;color:var(--soft)">
  <svg width="12" height="9"><rect x=".5" y=".5" width="11" height="8" fill="none" stroke="#999"/><path d="M.5 .5l5.5 4 5.5-4" fill="none" stroke="#999"/></svg>Enter Email
</div>
<div class="abs head" style="left:924px;top:2380px;width:131px;height:46px;background:var(--white);display:flex;align-items:center;justify-content:center;gap:8px;font-size:14px;letter-spacing:2px">SUBSCRIBE <span>→</span></div>
<div class="abs" style="left:142px;top:2490px;width:915px;height:1px;background:var(--line)"></div>

<h4 class="abs head" style="left:142px;top:2540px;font-size:12px;color:var(--white);font-weight:500">CONTACT INFORMATION</h4>
<div class="foot-info" style="top:2576px"><svg width="12" height="14" viewBox="0 0 12 14"><path d="M2 1l3 3-1.5 2a8 8 0 0 0 4 4l2-1.5 3 3-2 2C5 13 -1 7 0 3z" fill="none" stroke="#ccc"/></svg>+1 555-014-2286</div>
<div class="foot-info" style="top:2614px"><svg width="12" height="9"><rect x=".5" y=".5" width="11" height="8" fill="none" stroke="#ccc"/><path d="M.5 .5l5.5 4 5.5-4" fill="none" stroke="#ccc"/></svg>info@pinecrestdetailing.com</div>
<div class="foot-info" style="top:2652px"><svg width="12" height="16" viewBox="0 0 12 16"><path d="M6 15S1 9 1 6a5 5 0 0 1 10 0c0 3-5 9-5 9z" fill="none" stroke="#ccc"/><circle cx="6" cy="6" r="2" fill="none" stroke="#ccc"/></svg><span>123, Orci varius natoque penatibus, Orci<br>varius natoque penatibus 123</span></div>

<nav class="foot-nav">
  <a style="top:2540px">HOME</a>
  <a style="top:2577px">SERVICES</a>
  <a style="top:2614px">BLOG</a>
  <a style="top:2651px">CONTACT US</a>
</nav>
<div class="abs" style="left:1040px;top:2542px;width:16px;height:16px;border-radius:50%;background:var(--white)"></div>
<div class="abs" style="left:1040px;top:2577px;width:16px;height:16px;background:var(--white)"></div>

<p class="abs" style="left:141px;top:2768px;font-size:10px;color:#bbb">Copyright © 2020 Pinecrest Mobile Detailing. All rights reserved.</p>
<div class="abs" style="left:1011px;top:2754px;width:44px;height:44px;border-radius:50%;background:#2a2a2a;display:flex;align-items:center;justify-content:center"><svg width="10" height="16"><path d="M5 15V1M1 5l4-4 4 4" stroke="#fff" fill="none"/></svg></div>

</body>
</html>
```